Beauty Salon Industry - Web Design Project

zQuarta is a well-funded start up developing an Online Marketing Platform for small businesses in Europe.
We require a large number of high quality business web designs for our business website builder. Our business websites are seamlessly integrated into our Online Marketing systems and therefore it is important for designers to comply with our Design Guidelines.
This is our second contest and it will focus on the beauty salon industry. We will be running contents every 2-3 weeks for a new industry. Last month, we ran a contest for Builder website designs with 3 top prizes (plus £10 per variation) and we also paid out £25 per design for 20+ entries from designers who did not win the top prizes. So we encourage all entries!
We have included a wire frame this time to encourage you to be as creative as possible with your designs and layout while respecting the following guidelines:
1) You CAN change the layout as much as you like. If you think a vertical menu would look better, then use it. If you think the design would benefit from moving an element to a different location, then you can do that too.
2) You must include ALL the elements in the wire frame in your design.(e.g. latest 2 news entries, a testimonial, 1 gallery image, carousel etc...). Please make sure you have looked through the wire frame and know what is required. Entries that do not include all the elements will not qualify to win.
3) So remember, you CAN change the layout as much as you like but DO NOT remove any elements nor move them to a different page.
4) You may change the size and style of the carousel image. We would like to see as many variations of this as possible.
We are rewarding 3 prizes, and would like the winning designer to design the internal pages to the new design.
As always, if we think your designs could be incorporated into our system, but you do not win the competition, we will reward £25. Therefore, we encourage designers to submit as many designs as possible as we may award up to 25 designs.
Judging criteria : -
1) Visual Design
2) Layout must adhere to best practices and wireframe. If you decide to move elements around significantly please provide reason
3) Functional, informative and drives calls to action
Updates
As usual:
1st place = £350
2nd place = £250
3rd place = £150
Good luck!
Very happy with all the designs submitted so far, and will provide feedback ASAP.
We would like to see you try arranging the elements differently. So please try different navigation types and layouts.
Thanks
Morris
Prize funds for 1st place has been slightly increased.
Thanks
Morris
We have already had some amazing designs submitted. Thanks.
Remember to play with the layout of the elements and try designs with a carousel/slider that is in portrait not just in landscape.
Thanks everyone!
Morris
Hi everyone, we are really enjoying looking through the designs.
We have one NEW requirement. If you have used an image from http://www.frelik-example.com/ in your design, could you please replace it with another.
We are not associated with them.
Thank you.
I have just sent a poll around the office to vote on all the designs and hope to have the results soon.
Good luck and I hope to see all your great designs for our next project in a couple of weeks.
Morris
Hi everyone, we hope you have had a good holiday season. We will be rewarding the prizes very soon, hopefully today or tomorrow.
Thanks
Morris
We are currently going through all the designs that did not win our competition and will be contacting the designers of the designs we would like to use in our system, so please keep an eye on your inbox over the next few days.
Thank you
Morris
Target Market(s)
Beauty Salon Industry
Industry/Entity Type
Beauty Salon
Look and feel
Each slider illustrates characteristics of the customer's brand and the style your logo design should communicate.

```html
<!DOCTYPE html>
<html lang="en">
<head>
<meta charset="utf-8">
<title>Velvet Wave – Hair and Urban salon</title>
<link rel="stylesheet" href="https://fonts.googleapis.com/css2?family=Dancing+Script:wght@500&family=Quicksand:wght@500;700&display=swap">
<style>
:root{
  --header:#3d3d3d;
  --header-dark:#2f2f2f;
  --nav:#3a2b45;
  --nav-dark:#2a1f33;
  --active:#6b3f8c;
  --band:#2b2b2b;
  --body:#494949;
  --panel:#6f6672;
  --panel-light:#7c7480;
  --promo:#7a7a7a;
  --promo-frame:#a9a9a9;
  --text:#ffffff;
  --muted:#dedede;
  --quote:#8e8e8e;
  --accent:#c9a8e0;
  --footer:#353535;
  --bottom:#4f4f4f;
}
*{margin:0;padding:0;box-sizing:border-box}
html,body{width:935px;height:1200px;overflow:hidden;background:var(--body)}
body{position:relative;font-family:"Quicksand",sans-serif;color:var(--text)}
.abs{position:absolute}
.script{font-family:"Dancing Script",cursive}

.site-header{left:0;top:0;width:935px;height:109px;background:linear-gradient(var(--header),var(--header-dark))}
.brand{left:101px;top:34px}
.brand-name{font-family:"Dancing Script",cursive;font-size:30px;line-height:32px;color:var(--text)}
.brand-sub{font-size:21px;font-weight:700;line-height:26px;color:var(--text)}
.contact{left:779px;top:32px;font-size:19px;font-weight:700;line-height:30px}
.contact span{display:block}
.contact .book{font-size:22px}

.main-nav{left:0;top:109px;width:935px;height:54px;background:linear-gradient(var(--nav),var(--nav-dark))}
.nav-active{left:141px;top:109px;width:136px;height:87px;background:repeating-linear-gradient(var(--active) 0 54px,#5a3578 54px 60px,#4a3058 60px 66px,#3e3345 66px 72px,#373039 72px 87px)}
.nav-item{top:121px;font-family:"Dancing Script",cursive;font-size:22px;color:var(--text)}
.nav-item.current{color:#e5d2f3}

.sub-band{left:0;top:163px;width:935px;height:61px;background:var(--band)}

.hero{left:0;top:224px;width:935px;height:372px}
.hero-slide{position:absolute;top:0;height:372px}

.panel-stripes{background:repeating-linear-gradient(#7b737f 0 6px,#686070 6px 12px)}
.intro{left:5px;top:607px;width:352px;height:284px;background:var(--panel)}
.intro .stripe-top{left:0;top:0;width:352px;height:40px}
.intro h2{left:16px;top:36px;font-family:"Dancing Script",cursive;font-weight:500;font-size:18px}
.intro p{left:18px;top:72px;width:320px;font-size:12.5px;line-height:15.5px;color:var(--muted);text-indent:22px}

.more-arrow{display:inline-block;width:36px;height:10px;vertical-align:middle}

.testimonial{left:371px;top:601px;width:555px;font-family:"Dancing Script",cursive;font-size:14px;line-height:14px;color:var(--quote)}

.news{left:363px;top:656px;width:381px;height:182px;background:var(--panel)}
.news-item{position:absolute;top:40px;width:180px}
.news-item h3{font-family:"Dancing Script",cursive;font-weight:500;font-size:17px;line-height:18px}
.news-item p{font-size:12.5px;line-height:14.5px;color:var(--muted)}
.news-more{left:143px;top:128px;font-size:12.5px;color:var(--muted)}
.news .stripe-bottom{left:0;top:150px;width:381px;height:32px}

.gallery-thumb{left:750px;top:654px;width:181px;height:226px}
.gallery-link{left:752px;top:887px;font-size:13px;color:var(--muted)}

.promo{left:379px;top:838px;width:311px;height:196px;background:repeating-linear-gradient(#bdbdbd 0 8px,#9a9a9a 8px 16px)}
.promo-inner{left:8px;top:20px;width:295px;height:152px;background:var(--promo);border:2px solid #d0d0d0}
.gift{left:16px;top:16px;width:138px;height:118px}
.promo-price{left:168px;top:12px;font-size:22px;font-weight:700;line-height:24px}
.promo-text{left:168px;top:38px;width:120px;font-size:15px;font-weight:700;line-height:15px}
.promo-cta{left:168px;top:92px;font-size:15px;line-height:15px;color:var(--accent)}

.hours{left:9px;top:911px;font-size:12.5px;line-height:16px}
.hours h4,.address h4{font-size:13px;font-weight:700;margin-bottom:14px}
.hours dl{display:grid;grid-template-columns:38px auto}
.address{left:181px;top:911px;font-size:12.5px;line-height:16px}
.address .map{margin-top:22px;font-weight:700}

.partners{left:0;top:1047px;width:935px;height:120px;background:linear-gradient(#2f2f2f,var(--footer) 60%,#3c3c3c)}
.partner{position:absolute;top:36px;height:58px;background:#ffffff;border:1px solid #cfcfcf}

.site-footer{left:0;top:1167px;width:935px;height:33px;background:var(--bottom);font-size:12.5px}
.site-footer .managed{left:675px;top:9px}
.site-footer .admin{left:883px;top:9px}
</style>
</head>
<body>

<header class="site-header abs">
  <div class="brand abs">
    <div class="brand-name">Velvet Wave</div>
    <div class="brand-sub">Hair and Urban salon</div>
  </div>
  <div class="contact abs"><span>040 05550187</span><span class="book">Book Now</span></div>
</header>

<nav class="main-nav abs" aria-label="Main"></nav>
<div class="nav-active abs"></div>
<a class="nav-item abs" style="left:70px">Home</a>
<a class="nav-item current abs" style="left:166px">Services</a>
<a class="nav-item abs" style="left:293px">Gallery</a>
<a class="nav-item abs" style="left:418px">Testimonials</a>
<a class="nav-item abs" style="left:570px">News</a>
<a class="nav-item abs" style="left:669px">About us</a>
<a class="nav-item abs" style="left:778px">Contact us</a>

<div class="sub-band abs"></div>

<section class="hero abs" aria-label="Carousel">
  <div class="hero-slide" style="left:0;width:308px;background:linear-gradient(135deg,#e4e0d8,#c9b9a6 55%,#8a5a3e)" role="img" aria-label="Model with voluminous red curly hair"></div>
  <div class="hero-slide" style="left:308px;width:322px;background:linear-gradient(160deg,#d9d4cc,#b8a38a 50%,#e6e2dc)" role="img" aria-label="Model with a sculpted blonde updo"></div>
  <div class="hero-slide" style="left:630px;width:305px;background:linear-gradient(200deg,#efece6,#a58565 45%,#d8d3cc)" role="img" aria-label="Model with a tall brunette beehive"></div>
</section>

<section class="intro abs">
  <div class="stripe-top panel-stripes abs"></div>
  <h2 class="abs">Let our hair and beauty skills blow you away</h2>
  <p class="abs">Lorem ipsum dolor sit amet, consectetuer adipiscing elit. Nam cursus. Morbi ut mi. Nullam enim leo, egestas id, condimentum at, laoreet mattis, massa. Sed eleifend nonummy diam. Praesent mauris ante, at, posuere sit amet, nibh. Duis tincidunt lectus quis dui viverra vestibulum... rhoncus, sem nunc gravida justo, quis eleifend arcu velit quis lacus. Morbi magna magna, tincidunt a, mattis non, imperdiet vitae, tellus. Sed odio est, auctor ac, sollicitudin in, consequat vitae, orci. Fusce id felis. Vivamus sollicitudin metus eget eros.</p>
  <svg class="more-arrow abs" style="left:300px;top:258px" viewBox="0 0 36 10"><path d="M0 2h4v6H0zM7 2h4v6H7zM14 2h4v6h-4zM21 2h5v6h-5zM28 0l8 5-8 5z" fill="#a49aab"/></svg>
</section>

<blockquote class="testimonial abs">Quote from the latest entry on Testimonial page:<br>Lorem ipsum dolor sit amet, consectetuer adipiscing elit. Nam cursus. Morbi ut mi. Nullam enim leo, egestas id, condimentum at, laoreet mattis, massa. Sed eleifend nonummy diam...- Nina Castell.
<svg class="more-arrow" viewBox="0 0 36 10"><path d="M0 2h4v6H0zM7 2h4v6H7zM14 2h4v6h-4zM21 2h5v6h-5zM28 0l8 5-8 5z" fill="#7e7e7e"/></svg></blockquote>

<section class="news abs">
  <div class="stripe-bottom panel-stripes abs"></div>
  <article class="news-item" style="left:8px">
    <h3>Book Now for Christmas</h3>
    <p>Our salon is usually busy for the woo weeks Duis tincidunt lectus quis dui viverra vestibulum... rhoncus, sem nunc gravida</p>
  </article>
  <article class="news-item" style="left:197px">
    <h3>Want to be a hair model?</h3>
    <p>The woo weeks Duis tincidunt lectus quis dui viverra vestibulum... rhoncus, sem nunc gravida</p>
  </article>
  <div class="news-more abs">More news <svg class="more-arrow" viewBox="0 0 36 10"><path d="M0 2h4v6H0zM7 2h4v6H7zM14 2h4v6h-4zM21 2h5v6h-5zM28 0l8 5-8 5z" fill="#a49aab"/></svg></div>
</section>

<div class="gallery-thumb abs" style="background:linear-gradient(160deg,#f1ede6,#d8cbb4 50%,#bfb3a2)" role="img" aria-label="Gallery photo of a model with long platinum waves"></div>
<div class="gallery-link abs">View Gallery <svg class="more-arrow" viewBox="0 0 36 10"><path d="M0 2h4v6H0zM7 2h4v6H7zM14 2h4v6h-4zM21 2h5v6h-5zM28 0l8 5-8 5z" fill="#a49aab"/></svg></div>

<aside class="promo abs">
  <div class="promo-inner abs">
    <div class="gift abs" style="background:linear-gradient(150deg,#8a55b5,#5b2c82)" role="img" aria-label="Purple gift box with white ribbon"></div>
    <div class="promo-price abs">25$</div>
    <div class="promo-text abs">Complimentary gift for first-time clients!</div>
    <div class="promo-cta abs">Book<br>Appointment<br>Now</div>
  </div>
</aside>

<section class="hours abs">
  <h4>Business Hours</h4>
  <dl>
    <dt>Mon.</dt><dd>9 a.m. - 5 p.m.</dd>
    <dt>Tue.</dt><dd>9 a.m. - 5 p.m.</dd>
    <dt>Wed.</dt><dd>9 a.m. - 5 p.m.</dd>
    <dt>Thu.</dt><dd>9 a.m. - 5 p.m.</dd>
    <dt>Fri.</dt><dd>9 a.m. - 5 p.m.</dd>
    <dt>Sat.</dt><dd>9 a.m. - 5 p.m.</dd>
  </dl>
</section>

<section class="address abs">
  <h4>VELVET Adress</h4>
  <address style="font-style:normal">12 Harlow Lane<br>London<br>W9 3QT</address>
  <div class="map">View map <svg class="more-arrow" viewBox="0 0 36 10"><path d="M0 2h4v6H0zM7 2h4v6H7zM14 2h4v6h-4zM21 2h5v6h-5zM28 0l8 5-8 5z" fill="#a49aab"/></svg></div>
</section>

<section class="partners abs" aria-label="Partner brands">
  <div class="partner" style="left:240px;width:77px"></div>
  <div class="partner" style="left:361px;width:86px"></div>
  <div class="partner" style="left:488px;width:87px"></div>
  <div class="partner" style="left:615px;width:87px"></div>
</section>

<footer class="site-footer abs">
  <span class="managed abs">Managed by zQuarta.com</span>
  <span class="admin abs">Admin</span>
</footer>

</body>
</html>
```